A new company focused on starting and investing in transformative businesses.

We need a simple and clean website with a few pages. we like marlowvest.com as a starting point. we want the landing page to be very simple with an option to click through on the top right into INVESTOR LOGIN. then we want to be able to scroll down to see more about our company.

Target Market(s)

professional

Coding

Coded - Design and coding required

Number of Pages Required

2 page

Font styles to use
Serif
Sans Serif

Requirements
Must have
• HALVERN BUILDERS logo (attached as a file) on the top with INVESTOR LOGIN as a click through on the right. Please model the click through from marlowvest.com. The description (also written in attached file) should be on the landing page. we do not want to have to scroll to read the description.

Then we can scroll down to read more about Halvern including the mission and the two types of businesses. More is detailed on the attached file called "Halvern Website Syntax"
Should not have
• should not be slow loading with lots of fancy graphics. should not be busy and with too many colors.

```html
<!DOCTYPE html>
<html lang="en">
<head>
<meta charset="utf-8">
<title>Halvern Builders</title>
<link rel="stylesheet" href="https://fonts.googleapis.com/css2?family=Poppins:wght@400;500;600&display=swap">
<style>
  :root {
    --brand-blue: #00579f;
    --accent-blue: #3d8fe0;
    --ink: #1b1b1b;
    --muted: #9a9ea4;
    --white: #ffffff;
    --page-bg: #ffffff;
  }
  * { box-sizing: border-box; margin: 0; padding: 0; }
  html, body {
    width: 768px; height: 1200px; overflow: hidden;
    background: var(--page-bg);
    font-family: "Poppins", sans-serif;
  }
  .site {
    position: absolute; top: 145px; left: 0;
    width: 768px; height: 910px;
    background: var(--white);
  }
  /* Hero */
  .hero { position: relative; height: 365px; overflow: hidden; }
  .hero-photo {
    position: absolute; inset: 0;
    background:
      radial-gradient(ellipse at 78% 8%, rgba(236,214,186,0.9), transparent 45%),
      linear-gradient(180deg, #8f8a86 0%, #a89a8e 30%, #c9c6c4 55%, #e4e8ee 78%, #eef2f7 100%);
  }
  .brand {
    position: absolute; display: flex; align-items: center; gap: 6px;
    font-weight: 500; line-height: 1.05; letter-spacing: 0.02em;
  }
  .brand-mark { width: 9px; height: 9px; background: currentColor; }
  .hero .brand { left: 66px; top: 34px; color: var(--brand-blue); font-size: 12px; }
  .investor-login {
    position: absolute; left: 623px; top: 36px; width: 85px; height: 21px;
    border-radius: 11px; background: var(--brand-blue); color: var(--white);
    font-size: 7px; font-weight: 500; display: flex; align-items: center; justify-content: center;
    text-decoration: none;
  }
  .hero-title {
    position: absolute; left: 0; right: 0; top: 153px;
    text-align: center; color: var(--ink);
    font-size: 22px; font-weight: 500; line-height: 31px;
  }
  .scroll-cue { position: absolute; left: 376px; top: 340px; }

  /* About */
  .about { position: relative; height: 393px; }
  .mission { position: absolute; left: 54px; top: 65px; width: 333px; height: 250px; }
  .mission svg { position: absolute; inset: 0; }
  .mission-title {
    position: absolute; left: 0; right: 20px; top: 46px; text-align: center;
    color: var(--white); font-size: 22px; font-weight: 500;
  }
  .mission-rule { position: absolute; left: 97px; top: 80px; width: 79px; height: 2px; background: var(--accent-blue); }
  .mission-text {
    position: absolute; left: 30px; right: 40px; top: 101px; text-align: center;
    color: var(--white); font-size: 15px; line-height: 22px;
  }
  .focus { position: absolute; left: 421px; width: 300px; }
  .focus-ground { top: 93px; }
  .focus-special { top: 205px; }
  .focus-title { color: var(--brand-blue); font-size: 20px; font-weight: 500; line-height: 26px; }
  .focus-rule { width: 68px; height: 2px; background: var(--accent-blue); margin-bottom: 4px; }
  .focus-text { color: var(--muted); font-size: 10px; line-height: 15.3px; }

  /* Footer */
  .footer { position: absolute; left: 0; top: 758px; width: 768px; height: 152px; background: var(--brand-blue); color: var(--white); }
  .footer .brand { left: 154px; top: 45px; font-size: 14px; }
  .footer-contact { position: absolute; left: 489px; top: 41px; font-size: 12px; line-height: 17.3px; font-weight: 500; }
  .footer-rule { position: absolute; left: 30px; top: 124px; width: 708px; height: 2px; background: var(--white); }
  .copyright { position: absolute; left: 0; right: 0; top: 133px; text-align: center; font-size: 7px; font-weight: 500; }
</style>
</head>
<body>
<div class="site">
  <header class="hero">
    <div class="hero-photo" role="img" aria-label="Softly faded photo of a hand holding a pen over a printed bar chart, with glasses and notebooks on a desk"></div>
    <div class="brand"><span class="brand-mark"></span><span>HALVERN<br>BUILDERS</span></div>
    <a class="investor-login" href="#">Investor Login</a>
    <h1 class="hero-title">Halvern Builders is an entrepreneurial<br>firm focused on building and growing<br>transformational companies</h1>
    <svg class="scroll-cue" width="16" height="10" viewBox="0 0 16 10"><path d="M1.5 1.5 L8 8 L14.5 1.5" fill="none" stroke="#00579f" stroke-width="2" stroke-linecap="round" stroke-linejoin="round"/></svg>
  </header>

  <section class="about">
    <div class="mission">
      <svg width="333" height="250" viewBox="0 0 333 250"><path d="M38 0 L285 13 Q315 15 322 48 L331 195 Q333 235 295 237 L30 249 Q2 250 1 215 L0 40 Q0 -2 38 0 Z" fill="#00579f"/></svg>
      <h2 class="mission-title">Our mission</h2>
      <div class="mission-rule"></div>
      <p class="mission-text">Our mission is to build meaningful businesses that create enduring value by impacting people in a measurable way.</p>
    </div>
    <div class="focus focus-ground">
      <h3 class="focus-title">Ground Up</h3>
      <div class="focus-rule"></div>
      <p class="focus-text">Our ground up business applies a proven analytic process to identify value edge, a form of competitive advantage. We architect transformational companies and are deliberate in creating the foundation necessary to lead an industry.</p>
    </div>
    <div class="focus focus-special">
      <h3 class="focus-title">Special Opportunities</h3>
      <div class="focus-rule"></div>
      <p class="focus-text">We partner with exceptional teams that create value by transforming lives. Our investment focus includes large companies and spin-outs.</p>
    </div>
  </section>

  <footer class="footer">
    <div class="brand"><span class="brand-mark"></span><span>HALVERN<br>BUILDERS</span></div>
    <p class="footer-contact">Halvern Builders<br>For media inquiries, please contact<br>nora@halvernbuilders.com</p>
    <div class="footer-rule"></div>
    <p class="copyright">© 2020 all rights reserved</p>
  </footer>
</div>
</body>
</html>
```